Bed Company needs business card

Hello, we are a bed company that makes specialized magnets for beds. We are an alternative healing company. I need a modern and upscale business card. Please incorporate my logo for the card.

Accepted file formats are AI, EPS, and Press-Ready PDFS.

Please include all fonts or convert them to outlines regardless of file type.

If you are designing the card in Photoshop the file Must be 1200dpi.

I am open to anything for the business card.  I really like all of your designs and if you want to change the color of the logo, you can.  I will be making the final selection by Friday.  Thank You for all of your designs.  Feel Free to submit different color logos if you want.  

Reason: I will make a decision Final on Friday April 20th. 2012. Good Luck and Thank you all for the designs.

Target Market(s)

My target Market is people, who are looking for alternative healing.

Industry/Entity Type

Business

Requirements
Must have
• My logo must be incorporated. The front card must have

Name
Job Title

Address
Work
Cell
Fax
email
web

Just put in fake info for the card.

The back of the card. I want the logo on the back with color. I just want it to look modern and cool.

```html
<!DOCTYPE html>
<html lang="en">
<head>
<meta charset="utf-8">
<title>Lodestone Rest — Business Card</title>
<link href="https://fonts.googleapis.com/css2?family=Arimo:wght@400;700&display=swap" rel="stylesheet">
<style>
  :root {
    --backdrop: #4a4a4a;
    --front-green: #52b848;
    --brand-dark: #0b6b2b;
    --band-green: #0a6e2a;
    --accent-green: #4fb548;
    --card-white: #ffffff;
    --text-white: #ffffff;
  }
  html, body {
    margin: 0;
    padding: 0;
    width: 1200px;
    height: 1000px;
    overflow: hidden;
    background: var(--backdrop);
    font-family: "Arimo", Arial, sans-serif;
  }
  .card {
    position: absolute;
    border-radius: 11px;
    overflow: hidden;
  }
  /* Front side */
  .card-front {
    left: 63px;
    top: 15px;
    width: 763px;
    height: 464px;
    background: var(--front-green);
  }
  .brand {
    position: absolute;
    display: flex;
    align-items: center;
    gap: 16px;
  }
  .brand-mark {
    flex: none;
  }
  .brand-name {
    font-weight: 700;
    white-space: nowrap;
  }
  .brand-tagline {
    position: absolute;
    font-weight: 400;
    white-space: nowrap;
  }
  .card-front .brand {
    left: 155px;
    top: 205px;
  }
  .card-front .brand-mark {
    width: 42px;
    height: 42px;
    background: var(--brand-dark);
  }
  .card-front .brand-name {
    font-size: 54px;
    color: var(--card-white);
  }
  .card-front .brand-tagline {
    left: 379px;
    top: 283px;
    font-size: 18px;
    letter-spacing: 1px;
    color: var(--brand-dark);
  }
  .website {
    position: absolute;
    left: 0;
    right: 0;
    text-align: center;
    letter-spacing: 5px;
    color: var(--brand-dark);
  }
  .card-front .website {
    top: 435px;
    font-size: 24px;
  }
  /* Back side */
  .card-back {
    left: 400px;
    top: 509px;
    width: 761px;
    height: 465px;
    background: var(--card-white);
  }
  .card-back .brand {
    right: 38px;
    top: 40px;
  }
  .card-back .brand-mark {
    width: 28px;
    height: 28px;
    background: var(--brand-dark);
  }
  .card-back .brand-name {
    font-size: 34px;
    color: var(--brand-dark);
  }
  .card-back .brand-tagline {
    right: 38px;
    top: 89px;
    font-size: 14px;
    letter-spacing: 0.5px;
    color: var(--brand-dark);
  }
  .person {
    position: absolute;
    left: 57px;
    top: 122px;
  }
  .person-name {
    font-size: 42px;
    color: var(--brand-dark);
    line-height: 1;
  }
  .person-title {
    font-size: 22px;
    color: var(--accent-green);
    margin-top: 6px;
  }
  .contact-band {
    position: absolute;
    left: 0;
    top: 211px;
    width: 100%;
    height: 220px;
    background: var(--band-green);
    color: var(--text-white);
    font-size: 22px;
  }
  .contact-line {
    position: absolute;
    white-space: nowrap;
  }
  .address-label { left: 37px; top: 37px; }
  .address-street { left: 134px; top: 37px; }
  .address-city { left: 134px; top: 68px; }
  .email { left: 64px; top: 105px; }
  .mobile { left: 436px; top: 48px; }
  .fax { left: 476px; top: 90px; }
  .card-back .website {
    top: 436px;
    font-size: 21px;
  }
</style>
</head>
<body>

<section class="card card-front" aria-label="Card front">
  <div class="brand">
    <span class="brand-mark"></span>
    <span class="brand-name">Lodestone Rest</span>
  </div>
  <span class="brand-tagline">Alternative Healing</span>
  <div class="website">www.website.com</div>
</section>

<section class="card card-back" aria-label="Card back">
  <div class="brand">
    <span class="brand-mark"></span>
    <span class="brand-name">Lodestone Rest</span>
  </div>
  <span class="brand-tagline">Alternative Healing</span>

  <div class="person">
    <div class="person-name">Name</div>
    <div class="person-title">Job title</div>
  </div>

  <div class="contact-band">
    <span class="contact-line address-label">address:</span>
    <span class="contact-line address-street">5345 Any Street west</span>
    <span class="contact-line address-city">Harborton , ST&nbsp; 54321</span>
    <span class="contact-line email">email: email@mailbox.com.au</span>
    <span class="contact-line mobile">mobile:&nbsp; 0400 318 726</span>
    <span class="contact-line fax">fax:&nbsp; 0400 318 726</span>
  </div>

  <div class="website">www.website.com</div>
</section>

</body>
</html>
```